I have a basketball training business combined with a strength training business. I train professio

I recently saw the cats that won the contest in the strength coach business card competition. I loved the design. I.want a card with my logo that calls attention to my clients as the card that won did to me. I would like to see if I could get a similar design. My logo is what I like although I must say I like the red and black design of the contest winner. perhaps if the smaller lettered portion of my logo coukd be separated from the larger KQT logo. It almost looks like 3M3. I like.the KQT Training and Development portion of it. I need help.

Training

```html
<!DOCTYPE html>
<html lang="en">
<head>
<meta charset="utf-8">
<title>KQT Training and Development – Business Card</title>
<link href="https://fonts.googleapis.com/css2?family=Roboto:wght@300;400;700&display=swap" rel="stylesheet">
<style>
  :root {
    --page-bg: #e9e9eb;
    --card-bg: #f7f7f9;
    --accent-red: #e8482c;
    --text-grey: #4a4a4a;
    --text-dark: #1e1e1e;
    --logo-dark: #333333;
  }
  * { margin: 0; padding: 0; box-sizing: border-box; }
  html, body {
    width: 1200px;
    height: 864px;
    overflow: hidden;
    background: var(--page-bg);
    font-family: "Roboto", Arial, sans-serif;
  }
  .canvas {
    width: 1200px;
    height: 864px;
    display: flex;
    align-items: center;
    justify-content: center;
  }
  .business-card {
    position: relative;
    width: 1000px;
    height: 572px;
    background: var(--card-bg);
    box-shadow: 0 6px 24px rgba(0,0,0,0.12);
  }
  .identity {
    position: absolute;
    top: 52px;
    right: 64px;
    text-align: right;
  }
  .identity__name {
    font-weight: 300;
    font-size: 40px;
    color: var(--accent-red);
    margin-bottom: 10px;
  }
  .identity__credential {
    font-weight: 300;
    font-size: 24px;
    color: var(--text-grey);
    line-height: 1.3;
  }
  .brand {
    position: absolute;
    left: 70px;
    top: 282px;
    display: flex;
    align-items: center;
    gap: 18px;
  }
  .brand__mark {
    width: 40px;
    height: 40px;
    background: var(--accent-red);
    flex: none;
  }
  .brand__name {
    font-weight: 700;
    font-size: 36px;
    color: var(--logo-dark);
    line-height: 1.1;
  }
  .contact {
    position: absolute;
    right: 64px;
    bottom: 60px;
    text-align: right;
    font-weight: 400;
    font-size: 24px;
    color: var(--text-dark);
  }
  .contact__row {
    display: flex;
    align-items: center;
    justify-content: flex-end;
    gap: 12px;
    margin-top: 14px;
  }
  .contact__icon { width: 22px; height: 26px; flex: none; }
</style>
</head>
<body>
<main class="canvas">
  <section class="business-card">
    <header class="identity">
      <h1 class="identity__name">Robin Marsh</h1>
      <p class="identity__credential">QSTA C-TR,MVS</p>
      <p class="identity__credential">PMSC (Performance Movement Strength Coach)</p>
    </header>

    <div class="brand">
      <span class="brand__mark"></span>
      <span class="brand__name">KQT Training and Development</span>
    </div>

    <div class="contact">
      <p class="contact__row">
        <span>555 014 2738</span>
        <svg class="contact__icon" viewBox="0 0 22 26" aria-hidden="true">
          <rect x="4" y="1" width="14" height="24" rx="2" fill="none" stroke="var(--accent-red)" stroke-width="2"/>
          <rect x="7" y="5" width="8" height="7" fill="var(--accent-red)"/>
          <circle cx="11" cy="19" r="1.8" fill="var(--accent-red)"/>
        </svg>
      </p>
      <p class="contact__row">
        <span>Www.robinmarshbasketball.com</span>
        <svg class="contact__icon" viewBox="0 0 22 26" aria-hidden="true">
          <circle cx="11" cy="13" r="10" fill="var(--accent-red)"/>
          <g fill="none" stroke="#fff" stroke-width="1.3">
            <ellipse cx="11" cy="13" rx="4.5" ry="10"/>
            <line x1="1" y1="13" x2="21" y2="13"/>
            <line x1="11" y1="3" x2="11" y2="23"/>
            <path d="M3 8 H19 M3 18 H19"/>
          </g>
        </svg>
      </p>
    </div>
  </section>
</main>
</body>
</html>
```